Flyer design for mental health and disability support work company.

The company name 'Harbourlight Disability'

we need a flyer design for our company.

Specialising
Harbourlight Disability is a new KWPS service aimed towards KWPS participants with psychosocial/mental health, intellectual, and cognitive disabilities. We also specialise in supporting participants with a history of being involved in the criminal justice system.

Our focus
Focusing on providing core KWPS supports for community participation, daily activities and supported independent living.

Authentic
Like-minded people passionate about wanting to make a difference in participants' lives.

Our aim is to provide holistic and empowering support targeted towards creating independence and guidance for all participants and families.

Over 35 years of experience working with people with a vast range of disabilities and individual support needs.

Extensive experience not only within KWPS but working with mainstream services within NSW Fairway, Health, Corrections and Parole, Housing, Civic Desk NSW, Pathmark, Brief Assist, QTOB and NSW court systems.

website www.harbourlightdisability.com.au
email for referrals send to - referrals@harbourlightdisability.com.au
for further information send to - hello@harbourlightdisability.com.au

number 1800 372 519

Font styles to use
Serif

Requirements
Should not have
• pictures with people that have disabilities

```html
<!DOCTYPE html>
<html lang="en">
<head>
<meta charset="utf-8">
<title>Harbourlight Disability – Flyer</title>
<link rel="stylesheet" href="https://fonts.googleapis.com/css2?family=Abril+Fatface&family=Archivo+Black&family=Montserrat:wght@400;500&display=swap">
<style>
  :root {
    --navy: #0d3559;
    --navy-deep: #0a2c4b;
    --gold: #f1b61a;
    --sky: #78aadd;
    --sky-pale: #a9c7e6;
    --photo-dark: #2c5a86;
    --photo-light: #8fb4d8;
  }
  * { margin: 0; padding: 0; box-sizing: border-box; }
  html, body { width: 850px; height: 1200px; overflow: hidden; background: var(--navy); }
  .flyer {
    position: relative; width: 850px; height: 1200px; overflow: hidden;
    background: var(--navy);
    font-family: "Montserrat", Arial, sans-serif;
  }
  .hero-photo {
    position: absolute; left: 0; top: 0; width: 850px; height: 428px;
    background: linear-gradient(120deg, var(--photo-light) 0%, var(--photo-dark) 45%, var(--photo-light) 100%);
  }
  .brand-badge {
    position: absolute; left: 601px; top: 334px; width: 196px; height: 196px;
    border-radius: 50%; background: var(--navy); border: 3px solid var(--sky);
    display: flex; align-items: center; justify-content: center; text-align: center;
  }
  .brand-name {
    font-family: "Abril Fatface", Georgia, serif; font-weight: 400;
    color: var(--sky-pale); font-size: 21px; line-height: 1.15; letter-spacing: 0.5px;
  }
  .intro {
    position: absolute; left: 43px; top: 440px; width: 545px;
    color: var(--gold); font-size: 18.5px; line-height: 24px;
  }
  .section-band {
    position: absolute; left: 0; width: 355px; height: 49px;
    font-family: "Abril Fatface", Georgia, serif; font-size: 41px; line-height: 49px;
    color: var(--navy); padding-left: 54px;
  }
  .band-gold { background: var(--gold); }
  .band-sky { background: var(--sky); }
  .section-text {
    position: absolute; left: 62px; width: 300px;
    font-size: 18.5px; line-height: 24px;
  }
  .text-gold { color: var(--gold); }
  .text-sky { color: var(--sky); }
  .figure-frame {
    position: absolute; left: 461px; top: 562px; width: 347px; height: 337px;
    border: 3px solid var(--sky);
    background: linear-gradient(160deg, var(--navy-deep) 0%, #3d6f9e 60%, var(--sky) 100%);
  }
  .experience {
    position: absolute; left: 60px; top: 924px; width: 735px;
    color: var(--gold); font-size: 18.2px; line-height: 24px;
  }
  .experience p + p { margin-top: 13px; }
  .cta-band {
    position: absolute; left: 0; top: 1123px; width: 850px; height: 57px;
    background: var(--gold); text-align: center;
    font-family: "Archivo Black", Arial, sans-serif; font-size: 45px; line-height: 57px;
    color: var(--navy); letter-spacing: 1px;
  }
</style>
</head>
<body>
<main class="flyer">
  <div class="hero-photo" role="img" aria-label="Blue-toned photo of a support worker in conversation with a client"></div>

  <div class="brand-badge">
    <span class="brand-name">HARBOURLIGHT<br>DISABILITY</span>
  </div>

  <p class="intro">Harbourlight Disability is a new KWPS service aimed toward KWPS participants with a history of criminal justice, psychosocial/-mental health, intellectual, and cognitive disabilities.</p>

  <h2 class="section-band band-gold" style="top:536px;">Our focus</h2>
  <p class="section-text text-gold" style="top:596px;">Focusing on providing core KWPS supports for community participation, daily activities and supported independent living.</p>

  <h2 class="section-band band-sky" style="top:710px;">Authentic</h2>
  <p class="section-text text-sky" style="top:770px; width:305px;">Likeminded people wanting to make a difference in participant's lives.</p>

  <h2 class="section-band band-gold" style="top:861px;">Our experience</h2>

  <div class="figure-frame" role="img" aria-label="Light blue illustration of a seated figure hugging their knees"></div>

  <div class="experience">
    <p>Our aim to provide holistic and empowering supports targeted towards creating independence and guidance for all participants and families.</p>
    <p>Over 35 years of experience working with people that have psychosocial, intellectual, and cognitive disabilities.</p>
    <p>Experience in working with mainstream supports under, Fairway, NSW Carewell, Corrections, Housing, Civic Desk NSW, Pathmark, Brief Assist and Court processes.</p>
  </div>

  <div class="cta-band">CALL NOW</div>
</main>
</body>
</html>
```